RWT Business Cards

We need to design new business cards for our company. We are a Managed Discretionary Account (MDA) adviser based in Sydney Australia. We have distinct corporate colour pallet which will be provided and various logo formats. I will also include our current business card design as a guide only to what we have accepted previously. The final design should convey financial professionalism and experience as well as the necessary company information.

Target Market(s)

High Net Worth and Professional Investors

Industry/Entity Type

Financial

Font styles to use
Serif

```html
<!DOCTYPE html>
<html lang="en">
<head>
<meta charset="utf-8">
<title>RWT Capital Partners – Business Card</title>
<link href="https://fonts.googleapis.com/css2?family=Arvo:wght@400;700&display=swap" rel="stylesheet">
<style>
  :root {
    --bg: #e9e6e1;
    --card-white: #ffffff;
    --brand-green: #1a7d16;
    --accent-sage: #c9d79a;
    --ink: #1f1f1f;
    --rule: #c8c8c8;
    --on-green: #ffffff;
  }
  * { box-sizing: border-box; margin: 0; padding: 0; }
  html, body { width: 1200px; height: 461px; overflow: hidden; }
  body {
    background: var(--bg);
    font-family: "Arvo", Georgia, serif;
    color: var(--ink);
    position: relative;
  }
  .card {
    position: absolute;
    top: 70px;
    width: 555px;
    height: 320px;
    box-shadow: 0 4px 14px rgba(0,0,0,0.25);
    overflow: hidden;
  }
  .card-front { left: 30px; background: var(--card-white); }
  .card-back  { left: 615px; background: var(--brand-green); }

  /* Front */
  .brand-name {
    position: absolute;
    left: 30px;
    top: 110px;
    width: 270px;
    text-align: center;
    font-weight: 700;
    font-size: 26px;
    line-height: 1.25;
    color: var(--brand-green);
  }
  .divider {
    position: absolute;
    left: 316px; top: 40px;
    width: 1px; height: 190px;
    background: var(--rule);
  }
  .contact-block { position: absolute; left: 330px; top: 36px; }
  .person-name { font-size: 19px; font-weight: 700; color: var(--brand-green); line-height: 1.2; }
  .person-role { font-size: 13px; line-height: 1.35; }
  .contact-list { list-style: none; margin-top: 16px; }
  .contact-list li {
    display: flex; align-items: center;
    font-size: 13px; line-height: 1.6;
  }
  .contact-list svg { width: 12px; height: 12px; margin-right: 8px; flex: none; }
  .address-band {
    position: absolute; left: 0; bottom: 0;
    width: 100%; height: 58px;
    background: var(--brand-green);
    border-top: 5px solid var(--accent-sage);
    color: var(--on-green);
    font-size: 14px;
    display: flex; align-items: center; justify-content: center;
  }

  /* Back */
  .back-info {
    position: absolute; left: 0; top: 128px; width: 100%;
    text-align: center;
    color: var(--on-green);
  }
  .reg-numbers { font-size: 18px; }
  .reg-numbers .sep { display: inline-block; width: 1px; height: 18px; background: rgba(255,255,255,0.5); margin: 0 12px; vertical-align: middle; }
  .web { font-size: 19px; letter-spacing: 1.5px; margin-top: 8px; }
  .web small { font-size: 14px; }
</style>
</head>
<body>
  <section class="card card-front">
    <div class="brand-name">RWT Capital<br>Partners</div>
    <div class="divider"></div>
    <div class="contact-block">
      <div class="person-name">Owen Hartley</div>
      <div class="person-role">Managing Director<br>Chief Investment Officer</div>
      <ul class="contact-list">
        <li><svg viewBox="0 0 12 12"><circle cx="6" cy="6" r="5.5" fill="#3aa0d8"/></svg>owen.hartley42</li>
        <li><svg viewBox="0 0 12 12"><circle cx="6" cy="6" r="5.4" fill="none" stroke="#333" stroke-width="1.1"/><path d="M4 3.2 L5.2 4.6 L4.6 5.4 Q5.4 7 6.8 7.6 L7.6 7 L9 8.2 Q8.2 9.4 7 9 Q3.6 7.6 3 4.4 Q3.2 3.4 4 3.2Z" fill="#333"/></svg>1300-555-014</li>
        <li><svg viewBox="0 0 12 12"><circle cx="6" cy="6" r="5.4" fill="none" stroke="#333" stroke-width="1.1"/><path d="M4 3.2 L5.2 4.6 L4.6 5.4 Q5.4 7 6.8 7.6 L7.6 7 L9 8.2 Q8.2 9.4 7 9 Q3.6 7.6 3 4.4 Q3.2 3.4 4 3.2Z" fill="#333"/></svg>+61 (0)4-5550-1937</li>
        <li><svg viewBox="0 0 12 12"><path d="M1 4.5 L6 1.5 L11 4.5 V10.5 H1Z" fill="#333"/><path d="M1.5 5 L6 8 L10.5 5" fill="none" stroke="#fff" stroke-width="0.9"/></svg>OH@rwtcapital.com.au</li>
        <li><svg viewBox="0 0 12 12"><circle cx="6" cy="6" r="5.2" fill="#333"/><path d="M1 6 H11 M6 1 V11 M6 1 Q2.8 6 6 11 M6 1 Q9.2 6 6 11" fill="none" stroke="#fff" stroke-width="0.7"/></svg>www.rwtcapital.com.au</li>
      </ul>
    </div>
    <div class="address-band">Level 6, 12-14 Harbour Lane, Sydney NSW 2000 Australia</div>
  </section>

  <section class="card card-back">
    <div class="back-info">
      <div class="reg-numbers">ABN: 12 345 678 901<span class="sep"></span>AFSL: 512043</div>
      <div class="web">www.rwtcapital<small>.com.au</small></div>
    </div>
  </section>
</body>
</html>
```